Brand new start up connecting advertisers to the gaming community needs a cool website design

The company is called Quenzly with the tagline "Gamers, Fans, and Brands". I connect the advertisers and their brands/services with sponsorship opportunities within the gaming community, which includes popular streamers, professional gamers and teams as well as venues that host popular events.

I need a website that's fun, eye-catching and playful but not at the expense of professionalism. I'm in the gaming space so some degree of playfulness within the site and context is desired.

As an example, I envision a plugin for the initial load screen where the letters of my logo (see uploaded files for visual) fall from the top of the screen upside down (hence the "quenzly") and bounce into place centered on the screen above the fold . Once that sequence concludes (a few seconds), it holds in place and then the letters turn into correct form to form the logo. After all that the tagline appears underneath. I think a 5 second total sequence of all this makes the most sense and it only loads when you initially visit.

I have other ideas but welcome yours. If you've worked in this esports/gaming environment before, I would love to hear your thoughts and suggestions. If you haven't, that's ok too.

Please keep in mind, I need to keep a professional tone throughout this project's design. Meridex 400 companies and the largest ad agencies in the world will be my clients. I need them to know that Quenzly is legit and credible not goofy and all "gamey"

Target Market(s)

it's two fold. The primary target will be adults 25-54 but a secondary target is streamers/gamers/video gaming community that is mostly male 12-34.

Industry/Entity Type

Advertising

Coding

Coded - Design and coding required

Number of Pages Required

4 page

Font styles to use
Sans Serif

Requirements
Must have
• A fun, playful website that is also professional.

I'm going to eventually drop in video examples of work I've done.

Cool backgrounds can either be developed or be from static pictures i own or use from large gaming tournaments showcasing the excitement around the experience.

Use whatever logo uploaded in the files that you think works best with your design
Nice to have
• Experiment with cool fonts as long as they are easy to read

Have fun with little "easter eggs" in the design such as things the visitors discovers when navigating the web page. Maybe when the cursor rolls over a letter in the logo, it reacts in a fun way such as inverting or expanding???

I'm open to anything fun as long as it doesn't dominate the experience. Playful should be limited to a few fun things but not be the epi-center of the experience.

If you want to explore other options or get better explanation on what this means, email me.
Should not have
• It shouldn't feel too business-like or static. I need a balance that leans professional with fun throughout that does NOT compromise the user's experience.

Do not play off of existing/traditional gaming clip art or proprietary trademarks like the velora symbol, Zentro logo, Moss Prowler monster, etc...

```html
<!DOCTYPE html>
<html lang="en">
<head>
<meta charset="utf-8">
<title>Quenzly — Gaming Community</title>
<link rel="stylesheet" href="https://fonts.googleapis.com/css2?family=Lexend:wght@400;500;600;700;800&display=swap">
<style>
  :root {
    --space-deep: #1c0a4a;
    --space-mid: #3a149a;
    --space-violet: #5a20c8;
    --space-blue: #1d3bb0;
    --ground: #121a63;
    --text-main: #ffffff;
    --text-muted: #c7b6ee;
    --accent-cyan: #2ec8f0;
  }
  * { margin: 0; padding: 0; box-sizing: border-box; }
  html, body {
    width: 1200px;
    height: 534px;
    overflow: hidden;
    background: var(--space-deep);
  }
  .hero {
    position: relative;
    width: 1200px;
    height: 534px;
    overflow: hidden;
    font-family: "Lexend", sans-serif;
    color: var(--text-main);
  }
  .hero-scene {
    position: absolute;
    inset: 0;
    background:
      radial-gradient(ellipse 190px 170px at 600px 330px, rgba(46, 200, 240, 0.75), rgba(46, 200, 240, 0) 100%),
      linear-gradient(180deg, var(--space-deep) 0%, var(--space-mid) 35%, var(--space-violet) 55%, var(--space-blue) 75%, var(--ground) 100%);
  }
  .brand {
    position: absolute;
    left: 34px;
    top: 32px;
    display: flex;
    align-items: center;
    gap: 6px;
    font-family: "Lexend", sans-serif;
    font-weight: 600;
    font-size: 15px;
    line-height: 1;
    color: var(--text-main);
  }
  .brand-dot {
    width: 7px;
    height: 7px;
    border-radius: 50%;
    background: var(--accent-cyan);
  }
  .main-nav {
    position: absolute;
    top: 31px;
    left: 0;
    width: 100%;
    height: 20px;
  }
  .main-nav a {
    position: absolute;
    top: 0;
    font-size: 13px;
    font-weight: 500;
    color: var(--text-muted);
    text-decoration: none;
  }
  .main-nav a.is-active { color: var(--text-main); }
  .menu-toggle {
    position: absolute;
    left: 1131px;
    top: 36px;
    width: 34px;
    height: 12px;
  }
  .hero-title {
    position: absolute;
    top: 180px;
    left: 0;
    width: 100%;
    text-align: center;
    font-size: 49px;
    font-weight: 700;
    letter-spacing: -0.5px;
    line-height: 1;
  }
  .hero-lead {
    position: absolute;
    top: 259px;
    left: 0;
    width: 100%;
    text-align: center;
    font-size: 11.8px;
    font-weight: 500;
    line-height: 15.8px;
    letter-spacing: -0.15px;
  }
  .cta {
    position: absolute;
    left: 466px;
    top: 333px;
    width: 270px;
    height: 88px;
    text-decoration: none;
    color: var(--text-main);
  }
  .cta svg { position: absolute; inset: 0; }
  .cta-label {
    position: absolute;
    left: 0;
    top: 33px;
    width: 268px;
    text-align: center;
    font-size: 20px;
    font-weight: 600;
    letter-spacing: -0.3px;
  }
  .scroll-cue {
    position: absolute;
    left: 554px;
    top: 422px;
    width: 92px;
    height: 44px;
  }
</style>
</head>
<body>
  <main class="hero">
    <div class="hero-scene" role="img" aria-label="Illustrated alien planet landscape at night: purple sky with stars, falling comets and a striped planet, a glowing blue planet rising behind the horizon, and rocky cliffs with glowing pink crystals"></div>

    <header>
      <div class="brand">
        <span class="brand-dot" aria-hidden="true"></span>
        <span class="brand-name">Quenzly</span>
      </div>
      <nav class="main-nav">
        <a href="#" class="is-active" style="left:362px">home</a>
        <a href="#" style="left:451px">about</a>
        <a href="#" style="left:541px">sponsorship</a>
        <a href="#" style="left:668px">community</a>
        <a href="#" style="left:788px">contacts</a>
      </nav>
      <svg class="menu-toggle" viewBox="0 0 34 12" aria-label="Menu">
        <g stroke="#ffffff" stroke-width="1.6" stroke-linecap="round" fill="none">
          <line x1="1" y1="1" x2="33" y2="1"/>
          <line x1="4" y1="6" x2="30" y2="6"/>
          <line x1="1" y1="11" x2="33" y2="11"/>
        </g>
      </svg>
    </header>

    <h1 class="hero-title">Gaming Community</h1>
    <p class="hero-lead">
      Lorem ipsum dolor sit amet, consectetur adipiscing elit, sed do eiusmod tempor incididunt ut labore et dolore magna aliqua. Ut enim ad minim veniam,<br>
      quis nostrud exercitation ullamco laboris nisi ut aliquip ex ea commodo consequat. Duis aute irure dolor in reprehenderit in voluptate velit esse cillum dolore eu fugiat nulla pariatur.<br>
      Excepteur sint occaecat cupidatat non proident, sunt in culpa qui officia deserunt mollit anim id est laborum.
    </p>

    <a href="#" class="cta">
      <svg viewBox="0 0 270 88" aria-hidden="true">
        <path d="M2 3 L24 3 L26 24 L200 24 L219 40 L242 40 L267 53 L267 75 L241 75 L234 85 L214 85 L198 69 L26 69 L12 55 L10 26 L2 22 Z"
              fill="none" stroke="#ffffff" stroke-width="1.8" stroke-linejoin="round"/>
      </svg>
      <span class="cta-label">Find Out More</span>
    </a>

    <svg class="scroll-cue" viewBox="0 0 92 44" aria-label="Scroll down">
      <g fill="none" stroke="#ffffff" stroke-width="2.2" stroke-linejoin="miter">
        <path d="M1 12 L14 8 L10 14 L22 9 L45 40 L88 2"/>
        <path d="M25 12 L46 36"/>
      </g>
    </svg>
  </main>
</body>
</html>
```